Velmora Grid - Stock Certificate

We need a custom designed stock certificate that represents the look of our company logo but also have a cool look compared to a standard stock certificate. We thinking we want the logo in gold. Our website is https://www.velmoragridusa.example.

We are wanting the certificate to look very professional and really cool, we have sales agents that work for the company and we are creating a program by which the sales agents can gain ownership in the company. So the certificates need to have a very cool appeal and that provides a sense of pride in owning "Units" in Velmora Grid.
Updates

Project Deadline Extended
Reason: Extending so other board members can vote as well, thank you all!

Target Market(s)

Stock/Shareholders

Industry/Entity Type

It Company

Font styles to use
Script

Requirements
Must have
• Must look like a stock certificate, must use our logo which the psd file for it was attached.
Nice to have
• Nice to have the logo in gold

```html
<!DOCTYPE html>
<html lang="en">
<head>
<meta charset="utf-8">
<title>Velmora Grid – Stock Certificate</title>
<link rel="stylesheet" href="https://fonts.googleapis.com/css2?family=UnifrakturMaguntia&family=Pinyon+Script&family=Open+Sans:wght@400&family=Roboto:wght@400;700&display=swap">
<style>
  :root {
    --page-bg: #121212;
    --band-dark: #0b0b0b;
    --band-mid: #4a4a4a;
    --panel-light: #d6d6d6;
    --panel-mid: #b9b9b9;
    --panel-edge: #8c8c8c;
    --ink: #111111;
    --ink-soft: #2a2a2a;
    --gold: #e0a526;
    --rule: #555555;
  }
  * { margin: 0; padding: 0; box-sizing: border-box; }
  html, body { width: 1200px; height: 900px; overflow: hidden; background: var(--page-bg); }

  .canvas { position: relative; width: 1200px; height: 900px; overflow: hidden; }

  .certificate {
    position: absolute; left: 40px; top: 55px; width: 1120px; height: 790px;
    background: var(--band-dark); overflow: hidden;
  }
  .border-pattern {
    position: absolute; inset: 12px;
    background: radial-gradient(circle, var(--band-mid) 0%, #2b2b2b 60%, #1a1a1a 100%);
  }
  .panel {
    position: absolute; left: 70px; top: 62px; right: 72px; bottom: 67px;
    background: linear-gradient(135deg, var(--panel-light) 0%, var(--panel-mid) 55%, #cfcfcf 100%);
    border: 3px solid var(--panel-edge);
  }
  .corner-ornament {
    position: absolute; width: 80px; height: 80px; margin: -40px 0 0 -40px;
    background: radial-gradient(circle, #6a6a6a 0%, #2c2c2c 70%);
    border: 3px solid #9a9a9a;
    transform: rotate(45deg);
  }
  .corner-tl { left: 80px; top: 61px; }
  .corner-tr { left: 1066px; top: 61px; }
  .corner-bl { left: 80px; top: 730px; }
  .corner-br { left: 1066px; top: 730px; }

  .logo-badge {
    position: absolute; left: 471px; top: 20px; width: 176px; height: 176px;
    border-radius: 50%;
    background: var(--band-dark); border: 4px solid #7a7a7a;
    display: flex; align-items: center; justify-content: center;
  }
  .logo-name {
    font-family: "Open Sans", sans-serif; font-size: 20px; color: var(--gold);
    letter-spacing: 1px;
  }

  .text { position: absolute; text-align: center; color: var(--ink); line-height: 1; white-space: nowrap; }
  .issuer, .location { font-family: "Open Sans", sans-serif; font-size: 18px; line-height: 24px; }
  .issuer { left: 118px; width: 350px; top: 122px; }
  .issuer small { display: block; font-size: 12.5px; line-height: 18px; }
  .location { left: 715px; width: 240px; top: 122px; }
  .location small { display: block; font-size: 18px; line-height: 26px; }

  .title {
    left: 0; width: 1120px; top: 188px;
    font-family: "UnifrakturMaguntia", serif; font-size: 112px; font-weight: 400; color: var(--ink);
    text-shadow: 3px 3px 0 #fff;
  }
  .script { font-family: "Pinyon Script", cursive; color: var(--ink-soft); font-size: 21px; }
  .certify { left: 0; width: 1120px; top: 306px; }
  .holder {
    left: 253px; width: 612px; top: 338px; height: 43px;
    font-family: "Roboto", sans-serif; font-weight: 700; font-size: 38px;
    border-bottom: 1.5px solid var(--rule);
  }
  .owner { left: 0; width: 1120px; top: 389px; }
  .shares {
    left: 354px; width: 408px; top: 420px; height: 31px;
    font-family: "Roboto", sans-serif; font-size: 24px;
    border-bottom: 1.5px solid var(--rule);
  }
  .terms { left: 100px; width: 920px; top: 468px; line-height: 26.5px; }
  .witness { left: 100px; width: 920px; top: 557px; line-height: 28px; }
  .blank { display: inline-block; border-bottom: 1px solid var(--rule); vertical-align: baseline; }

  .signature {
    top: 648px; width: 306px; padding-top: 6px;
    border-top: 1.5px solid var(--rule);
  }
  .signature-secretary { left: 140px; }
  .signature-president { left: 671px; }
</style>
</head>
<body>
<div class="canvas">
  <main class="certificate">
    <div class="border-pattern" role="img" aria-label="Ornamental guilloche border pattern in black and silver"></div>
    <section class="panel"></section>
    <div class="corner-ornament corner-tl" role="img" aria-label="Decorative corner medallion"></div>
    <div class="corner-ornament corner-tr" role="img" aria-label="Decorative corner medallion"></div>
    <div class="corner-ornament corner-bl" role="img" aria-label="Decorative corner medallion"></div>
    <div class="corner-ornament corner-br" role="img" aria-label="Decorative corner medallion"></div>

    <div class="logo-badge"><span class="logo-name">Velmora Grid</span></div>

    <p class="text issuer">Velmora Grid<small>Incorporated Under the Laws of the State of Texas</small></p>
    <p class="text location">Houston, Texas<small>United States of America</small></p>

    <h1 class="text title">Stock Certificate</h1>

    <p class="text script certify">This is to certify that</p>
    <p class="text holder">MARCUS HALE</p>
    <p class="text script owner">is the owner of</p>
    <p class="text shares">One Hundred (100) Shares</p>

    <p class="text script terms">fully paid and non-assessable shares of Velmora Grid transferrable only on the books of the<br>Corporation by the holder thereof in person or by a duly authorized Attorney<br>upon surrender of this Certificate properly endorsed.</p>
    <p class="text script witness">Witness, the seal of the Corporation and the signatures of its duly authorized officers<br>this <span class="blank" style="width:40px"></span> day of <span class="blank" style="width:125px"></span>, 2017.</p>

    <p class="text script signature signature-secretary">Secretary</p>
    <p class="text script signature signature-president">President</p>
  </main>
</div>
</body>
</html>
```